Borvix Letter head

Borvix is a young and energetic software development consultancy. We spend our time working with clients to turn what ever is in their heads in to software.
We are trying to create an image of a high class software boutique who build class leading bespoke solutions.
We need a sharp letter head that looks great on high quality media.
We like bold colours and distinctive design. So show us what you can do.
Industry/Entity Type
Software
Requirements
Must have
- Our company is based in the UK and are requried to have on the paper somewhere the following information:
* Registered company name: Borvix Ltd
* Registered company number
* VAT registration number
In addition we also want the following:
* An email address
* Telephone number
* Website address
An example of what some pages have in their footer is something like the following:
Borvix Ltd is registered in England and Wales. Reg. no: 4916275
Registered office: 48 Quillmore Road, Harwick Dunshire, HR43PL. Tel: 07442615093
You do not have to use this sentance but please make sure your design incorporates accommodates the requirements for UK based companies

```html
<!DOCTYPE html>
<html lang="en">
<head>
<meta charset="utf-8">
<title>Borvix Letterhead</title>
<link href="https://fonts.googleapis.com/css2?family=Jost:wght@400;500;600&display=swap" rel="stylesheet">
<style>
  :root {
    --bg: #b4b4b4;
    --brand-red: #c8102e;
    --cover-top: #a2a2a2;
    --cover-bottom: #7b7b7b;
    --paper: #f7f7f7;
    --ink: #2a2a2a;
    --muted: #6f6f6f;
    --frame: #9a9a9a;
    --cover-text: #e4e4e4;
  }
  * { box-sizing: border-box; margin: 0; padding: 0; }
  html, body { width: 1200px; height: 720px; overflow: hidden; }
  body {
    background: var(--bg);
    font-family: "Jost", "Futura", sans-serif;
    color: var(--ink);
    position: relative;
  }
  .sheet {
    position: absolute;
    top: 35px;
    width: 460px;
    height: 650px;
    box-shadow: 0 6px 18px rgba(0,0,0,0.25);
  }
  .cover {
    left: 110px;
    background: linear-gradient(160deg, var(--cover-top), var(--cover-bottom));
  }
  .cover-brand {
    position: absolute;
    left: 0; right: 0;
    top: 318px;
    text-align: center;
  }
  .wordmark {
    font-weight: 600;
    color: var(--brand-red);
    letter-spacing: 0.5px;
    text-transform: uppercase;
  }
  .cover .wordmark { font-size: 22px; }
  .cover-web {
    margin-top: 4px;
    font-size: 7.5px;
    color: var(--cover-text);
    letter-spacing: 0.4px;
  }
  .letter {
    left: 630px;
    background: var(--paper);
  }
  .letter-frame { position: absolute; inset: 0; }
  .letter-header {
    position: absolute;
    top: 34px;
    right: 30px;
    text-align: right;
  }
  .letter .wordmark { font-size: 19px; }
  .sender-details {
    margin-top: 8px;
    font-size: 5.2px;
    line-height: 1.45;
    color: var(--muted);
  }
  .sender-details strong { color: var(--ink); font-weight: 600; }
  .recipient {
    position: absolute;
    top: 80px;
    left: 52px;
    font-size: 8.6px;
    line-height: 1.3;
    font-style: normal;
  }
  .recipient strong { font-weight: 600; }
  .letter-body {
    position: absolute;
    top: 168px;
    left: 52px;
    width: 372px;
    font-size: 7.9px;
    line-height: 1.38;
    text-align: justify;
  }
  .letter-body p { margin-bottom: 9px; }
  .signature {
    margin-top: 26px;
    text-align: left;
    font-size: 8.6px;
    line-height: 1.3;
  }
  .signature strong { font-weight: 600; display: block; }
  .letter-footer {
    position: absolute;
    bottom: 20px;
    left: 40px;
    right: 40px;
    text-align: center;
    font-size: 5.4px;
    color: var(--muted);
    letter-spacing: 0.2px;
  }
</style>
</head>
<body>
  <section class="sheet cover">
    <div class="cover-brand">
      <div class="wordmark">Borvix</div>
      <div class="cover-web">www.borvix.com</div>
    </div>
  </section>

  <section class="sheet letter">
    <svg class="letter-frame" width="460" height="650" viewBox="0 0 460 650" aria-hidden="true">
      <g fill="none" stroke="var(--frame)" stroke-width="1.4">
        <path d="M16 8 V596 Q16 612 32 612 H430"/>
        <path d="M22 8 V592 Q22 606 36 606 H430"/>
      </g>
    </svg>

    <header class="letter-header">
      <div class="wordmark">Borvix</div>
      <div class="sender-details">
        <strong>Borvix Ltd.</strong> 48 Quillmore Road<br>
        Harwick Dunshire<br>
        HR43PL<br><br>
        07442615093<br>
        info@borvix.com
      </div>
    </header>

    <address class="recipient">
      <strong>Mr. Daniel Hart</strong><br>
      Managing Director<br>
      Northgate Investor<br>
      220 W. Elm Street<br>
      United Kingdom
    </address>

    <div class="letter-body">
      <p>Lorem Ipsum is simply dummy text for printing and typesetting industry. Lorem Ipsum has been the industry's standard dummy text since the 1500s, when an unknown printer galley of type and scrambled it to make a type specimen book. It has survived not only manual but also the leap into electronic typesetting, remaining essentially unchanged. It was popularised in the 1960s with the release of Typeset sheets containing Lorem Ipsum pass and more recently with desktop publishing software like Quarto Layout including version 6.9 of Lorem Ipsum.</p>
      <p>Contrary to popular belief, Lorem Ipsum is not simply random text. It has roots in a piece of classical Latin literature from 45 BC, making it over 2000 years old. Edwin Marlow, a professor at Ashbury College in discovered the undoubtable source. Lorem Ipsum comes from section 1.10.32 and 1.10.33 of "de Rebus Claris et Obscuris" (The Extremes of Good and Evil) by Tavio Brenn, written in 45 BC. This book is a treatise on the theory of ethics very popular during Renaissance.</p>
      <p>Thank you for being one of our valued customers.</p>
      <div class="signature">
        <strong>Name Here</strong>
        CEO
      </div>
    </div>

    <footer class="letter-footer">
      Borvix Ltd &nbsp;|&nbsp; Reg. No.: 4916275 Registered in England and Wales &nbsp;|&nbsp; VAT Reg No.: GB 312 5570 84 &nbsp;|&nbsp; www.borvix.com
    </footer>
  </section>
</body>
</html>
```